Lumora Business Card Design

hello,
we are looking for a business card design for our Fintech Company. We are credit card processing company that is also expanding in to the crypto market. We will be focusing on crypto processing, with a crypto wallet and crypto exchange. We like the purple in the logo. We want something modern and sophisticated but at the same time simple and trust worthy to work with banks.

Industry/Entity Type

Fintech

Logo Text

Lumora

```html
<!DOCTYPE html>
<html lang="en">
<head>
<meta charset="utf-8">
<title>Lumora Business Card</title>
<link href="https://fonts.googleapis.com/css2?family=Poppins:wght@400;600&display=swap" rel="stylesheet">
<style>
  :root {
    --brand-blue: #2433ff;
    --ink-navy: #13286e;
    --paper: #ffffff;
    --page-bg: #ffffff;
    --card-edge: #e6e8ef;
  }
  * { margin: 0; padding: 0; box-sizing: border-box; }
  html, body {
    width: 1200px; height: 1200px; overflow: hidden;
    background: var(--page-bg);
    font-family: "Poppins", sans-serif;
  }
  .card {
    position: absolute;
    left: 324px;
    width: 560px;
    height: 330px;
    border-radius: 19px;
  }
  .card--front { top: 266px; background: var(--paper); border: 1px solid var(--card-edge); }
  .card--back { top: 664px; background: var(--brand-blue); }

  .brand-name {
    position: absolute;
    font-weight: 600;
    line-height: 1;
    letter-spacing: -2px;
  }
  .card--front .brand-name {
    left: 37px; top: 39px;
    font-size: 52px;
    color: var(--ink-navy);
  }
  .card--back .brand-name {
    left: 0; right: 0; top: 132px;
    text-align: center;
    font-size: 62px;
    color: var(--paper);
  }

  .person-name {
    position: absolute;
    right: 38px; top: 128px;
    font-size: 27px; line-height: 1;
    font-weight: 400;
    color: var(--brand-blue);
    white-space: nowrap;
  }
  .person-role {
    position: absolute;
    right: 38px; top: 158px;
    font-size: 15.5px; line-height: 1;
    color: var(--ink-navy);
    white-space: nowrap;
  }
  .divider {
    position: absolute;
    left: 37px; top: 167px;
    width: 324px; height: 1px;
    background: var(--brand-blue);
  }

  .contact-list {
    position: absolute;
    left: 37px; top: 211px;
    list-style: none;
    font-size: 14.5px; line-height: 17px;
    color: var(--ink-navy);
    white-space: nowrap;
  }
  .contact-list li { display: flex; align-items: center; gap: 5px; }
  .contact-icon { width: 11px; height: 11px; flex: none; fill: var(--brand-blue); }
  .contact-icon--outline { fill: none; stroke: var(--brand-blue); stroke-width: 0.8; }

  .back-url {
    position: absolute;
    left: 0; right: 0; top: 282px;
    text-align: center;
    font-size: 13px; line-height: 1;
    color: var(--paper);
  }
</style>
</head>
<body>
  <section class="card card--front">
    <div class="brand-name">Lumora</div>
    <div class="person-name">Dana WILDE</div>
    <div class="person-role">Creative Designer</div>
    <div class="divider"></div>
    <ul class="contact-list">
      <li>
        <svg class="contact-icon" viewBox="0 0 12 12" aria-hidden="true"><path d="M2.5 0.5l2 2.2-1 1.3c.7 1.6 1.9 2.9 3.5 3.7l1.2-1 2.3 2-1.3 1.8C5 10 1.5 6.2 1 1.6z"/></svg>
        <span>0216 555 01 23</span>
      </li>
      <li>
        <svg class="contact-icon" viewBox="0 0 12 12" aria-hidden="true"><path d="M0 2.5h12v7H0z"/><path d="M0.8 3.2L6 6.8l5.2-3.6" fill="none" stroke="#fff" stroke-width="0.8"/></svg>
        <span>hello@lumorapay.com</span>
      </li>
      <li>
        <svg class="contact-icon contact-icon--outline" viewBox="0 0 12 12" aria-hidden="true"><circle cx="6" cy="6" r="5.2"/><ellipse cx="6" cy="6" rx="2.3" ry="5.2"/><path d="M0.8 6h10.4M1.6 3.3h8.8M1.6 8.7h8.8"/></svg>
        <span>www.lumorapay.com</span>
      </li>
      <li>
        <svg class="contact-icon" viewBox="0 0 12 12" aria-hidden="true"><path d="M6 0.3a4 4 0 0 1 4 4c0 3-4 7.5-4 7.5S2 7.3 2 4.3a4 4 0 0 1 4-4zm0 2.4a1.6 1.6 0 1 0 0 3.2 1.6 1.6 0 0 0 0-3.2z"/></svg>
        <span>Merkez : Yildiz Mah. Lale Cad.</span>
      </li>
    </ul>
  </section>

  <section class="card card--back">
    <div class="brand-name">Lumora</div>
    <div class="back-url">www.lumorapay.com</div>
  </section>
</body>
</html>
```